Zub Programming Video Tutorial Blog

Please be aware I am flexible with budget, I will increase it for great design thanks

A blog (wordpress) design required for video blogging teaching Zub Programming (creating quorbit apps). There are 4 pages required to be designed, the landing page where user submit their name and email (also shows an intro video), the main video blogging page (with beautiful video placeholder), a normal text blog page with big image at the top of each post and finally the portfolio page. The portfolio is where the tutor showcase all his previous developed apps and other projects to show his expertise.

The colour combination preferred are a mixture of blue and orange but we are open to other beautiful color combinations. Minimalistic design with lots of white and clare objectives for each page. The design should reflect the purpose of the website, someone who cannot read english landing on the page should immediately realise the page is made for learning to design quorbit apps.

I like curves and round corners, especially comment and portfolio pages with curves etc thanks

The blog domain will be brelvanta.example
Updates

Target Market(s)

new programmer on the quorbit platform

Industry/Entity Type

Learning

Requirements
Must have
• quorbit image in the design
landing page has a video intro and Quorbit/vexa image
Nice to have
• curves. round corners and circular shapes

```html
<!DOCTYPE html>
<html lang="en">
<head>
<meta charset="utf-8">
<title>Brelvanta — Zub Programming Video Blog</title>
<link rel="stylesheet" href="https://fonts.googleapis.com/css2?family=Source+Sans+3:wght@300;400;600&display=swap">
<style>
  :root {
    --blue: #1a7fd4;
    --blue-dark: #0a5fb0;
    --orange-light: #ffab3c;
    --orange: #f07a00;
    --peach-top: #ffe2c2;
    --peach-bottom: #f9b978;
    --ink: #555a5e;
    --ink-soft: #6b7074;
    --line: #dcdfe2;
    --panel: #f6f7f8;
    --white: #ffffff;
    --badge: #b9bdc1;
    --footer: #f2f3f4;
  }
  * { box-sizing: border-box; margin: 0; padding: 0; }
  html, body { width: 1200px; height: 1135px; overflow: hidden; }
  body {
    position: relative;
    background: var(--white);
    font-family: "Source Sans 3", "Helvetica Neue", Arial, sans-serif;
    color: var(--ink);
  }
  .top-rule { position: absolute; left: 0; top: 0; width: 1200px; height: 5px; background: #3f95e0; }

  .brand { position: absolute; left: 62px; top: 52px; display: flex; align-items: center; gap: 14px; }
  .brand-dot { width: 40px; height: 40px; border-radius: 50%; background: var(--orange); }
  .brand-name { font-size: 42px; font-weight: 600; color: var(--blue); letter-spacing: -0.5px; line-height: 1; }

  .auth { position: absolute; top: 27px; display: flex; gap: 8px; left: 916px; }
  .btn-login, .btn-signup {
    height: 38px; border-radius: 19px; font-size: 16px; display: flex; align-items: center; justify-content: center;
  }
  .btn-login { width: 88px; background: linear-gradient(#2f94e6, var(--blue-dark)); color: var(--white); }
  .btn-signup { width: 93px; background: linear-gradient(#f1f1f1, #d9d9d9); color: var(--ink); }

  .main-nav { position: absolute; top: 88px; right: 110px; display: flex; font-size: 20px; color: var(--ink); }
  .main-nav span { padding: 0 16px; border-left: 1px solid #c4c7ca; line-height: 24px; }
  .main-nav span:first-child { border-left: none; }

  .hero {
    position: absolute; left: 60px; top: 135px; width: 1074px; height: 442px;
    border-radius: 18px; background: linear-gradient(180deg, var(--orange-light), var(--orange));
  }
  .partner-strip {
    position: absolute; left: 60px; top: 560px; width: 1072px; height: 89px;
    border: 1px solid var(--line); border-top: none; border-radius: 0 0 16px 16px;
    background: linear-gradient(#ffffff, #f4f5f6);
  }
  .partner-badge { position: absolute; top: 37px; height: 24px; border-radius: 5px; background: var(--badge); }

  .hero-title { position: absolute; left: 142px; top: 213px; font-size: 54px; font-weight: 300; color: var(--white); line-height: 1; }
  .hero-sub { position: absolute; left: 142px; top: 280px; font-size: 34px; font-weight: 300; color: var(--white); line-height: 1; }
  .hero-copy { position: absolute; left: 145px; top: 330px; width: 410px; font-size: 15px; line-height: 24.5px; color: var(--white); }
  .btn-hero {
    position: absolute; left: 148px; top: 416px; width: 139px; height: 40px; border-radius: 6px;
    background: linear-gradient(var(--peach-top), var(--peach-bottom)); color: #7a4a16;
    font-size: 16px; display: flex; align-items: center; justify-content: center;
    box-shadow: 0 1px 2px rgba(0,0,0,0.15);
  }
  .hero-arrows { position: absolute; left: 146px; top: 474px; }

  .device-back {
    position: absolute; left: 873px; top: 209px; width: 141px; height: 387px; border-radius: 24px;
    background: linear-gradient(135deg, #fafafa, #d9dcdf); border: 2px solid #b8bcc0;
  }
  .device-front {
    position: absolute; left: 656px; top: 155px; width: 222px; height: 470px; border-radius: 30px;
    background: linear-gradient(135deg, #ffffff, #dfe1e3); border: 2px solid #b0b4b8;
    box-shadow: 0 6px 14px rgba(0,0,0,0.18);
  }
  .device-front .screen {
    position: absolute; left: 13px; top: 64px; width: 193px; height: 340px;
    background: linear-gradient(#2a6fa8 0%, #c9ced3 12%, #d6dadd 70%, #1b3550 72%, #0e2236 100%);
  }
  .device-back .screen {
    position: absolute; left: 2px; top: 53px; width: 120px; height: 276px;
    background: linear-gradient(#1b8ad6 0%, #1b8ad6 8%, #d59a6a 40%, #6a3a2a 70%, #e8d8c0 100%);
  }

  .card {
    position: absolute; top: 683px; width: 343px; height: 290px; border-radius: 18px;
    border: 1px solid var(--line); background: linear-gradient(#ffffff 60%, #f7f8f9);
  }
  .card-title { position: absolute; left: 32px; top: 24px; font-size: 25px; font-weight: 300; color: var(--ink); }
  .card-lead { position: absolute; left: 32px; top: 66px; font-size: 16.5px; font-weight: 400; color: var(--ink); }
  .card-copy { position: absolute; left: 32px; top: 96px; width: 290px; font-size: 14.5px; line-height: 23px; color: var(--ink-soft); }
  .card-copy p + p { margin-top: 8px; }
  .btn-card {
    position: absolute; left: 32px; top: 233px; width: 107px; height: 32px; border-radius: 3px;
    background: linear-gradient(#2a8fe2, var(--blue-dark)); color: var(--white);
    font-size: 13.5px; display: flex; align-items: center; justify-content: center;
  }
  .video-frame {
    position: absolute; left: 19px; top: 58px; width: 309px; height: 213px; border-radius: 6px; background: #d2d4d6;
  }
  .video-still {
    position: absolute; left: 9px; top: 9px; width: 291px; height: 195px;
    background: linear-gradient(135deg, #3b8fd8, #9cc8ec 45%, #556270 70%, #2c6fb8);
  }
  .video-play { position: absolute; left: 125px; top: 78px; }

  .site-footer {
    position: absolute; left: 0; top: 1050px; width: 1200px; height: 85px;
    background: var(--footer); border-top: 1px solid #e2e4e6;
  }
  .legal { position: absolute; left: 63px; top: 29px; font-size: 13.5px; color: var(--ink); }
  .social { position: absolute; left: 1035px; top: 25px; display: flex; gap: 6px; }
  .social span { width: 27px; height: 27px; border-radius: 4px; background: #3a8fd8; }
  .social span:last-child { background: #3b5da8; }
</style>
</head>
<body>
  <div class="top-rule"></div>

  <header>
    <div class="brand"><span class="brand-dot"></span><span class="brand-name">Brelvanta</span></div>
    <div class="auth"><span class="btn-login">Login</span><span class="btn-signup">Sign Up</span></div>
    <nav class="main-nav"><span>Home</span><span>About Developer</span><span>Video</span><span>Blog</span><span>Contact</span></nav>
  </header>

  <section class="hero"></section>
  <div class="partner-strip">
    <div class="partner-badge" style="left:50px;width:62px"></div>
    <div class="partner-badge" style="left:140px;width:57px"></div>
    <div class="partner-badge" style="left:225px;width:77px"></div>
    <div class="partner-badge" style="left:333px;width:104px"></div>
    <div class="partner-badge" style="left:466px;width:60px"></div>
  </div>

  <h1 class="hero-title">Video Blogging</h1>
  <p class="hero-sub">Teaching Zub Programming..</p>
  <p class="hero-copy">Duis sed tellus et tortor vestibulum gravida. Praesent elementum elit at tellus. Curabitur metus ipsum, luctus eu, malesuada ut, tincidunt sed, diam.</p>
  <span class="btn-hero">READ MORE</span>
  <svg class="hero-arrows" width="40" height="28" viewBox="0 0 40 28" aria-label="Slide controls">
    <polyline points="14,3 4,14 14,25" fill="none" stroke="#fff" stroke-width="2.5"/>
    <polyline points="26,3 36,14 26,25" fill="none" stroke="#fff" stroke-width="2.5"/>
  </svg>

  <div class="device-back" role="img" aria-label="Quorbit handset showing a music app"><div class="screen"></div></div>
  <div class="device-front" role="img" aria-label="Quorbit handset showing a travel booking app"><div class="screen"></div></div>

  <article class="card" style="left:60px">
    <h2 class="card-title">What We Do</h2>
    <h3 class="card-lead">Phasellus felis dolor scelerisque</h3>
    <div class="card-copy">
      <p>Vivamus porttitor, g, purus nisi eleifend libero, a tempus libero lectus feugiat felis. Morbi diam mauris, viverra in, gravida eu, mattis in ante.</p>
      <p>Libero id ullamcorper nonummy, nibh ligula pulvinar metus, eget consectetuer</p>
    </div>
    <span class="btn-card">READ MORE</span>
  </article>

  <article class="card" style="left:426px">
    <h2 class="card-title" style="top:26px">Programming &amp; App</h2>
    <h3 class="card-lead" style="top:68px">Phasellus felis dolor scelerisque</h3>
    <div class="card-copy" style="top:98px">
      <p>Vivamus porttitor, g, purus nisi eleifend libero, a tempus libero lectus feugiat felis. Morbi diam mauris, viverra in, gravida eu, mattis in ante.</p>
      <p>Libero id ullamcorper nonummy, nibh ligula pulvinar metus, eget consectetuer</p>
    </div>
    <span class="btn-card">READ MORE</span>
  </article>

  <article class="card" style="left:792px">
    <h2 class="card-title" style="left:24px;top:20px">How it Works</h2>
    <div class="video-frame">
      <div class="video-still" role="img" aria-label="Video still of Quorbit handsets and a vexa tablet on a keyboard"></div>
      <svg class="video-play" width="60" height="60" viewBox="0 0 60 60" aria-label="Play video">
        <circle cx="30" cy="30" r="24" fill="#1e1e1e" stroke="#ffffff" stroke-opacity="0.5" stroke-width="2"/>
        <polygon points="24,19 41,30 24,41" fill="#ffffff"/>
      </svg>
    </div>
  </article>

  <footer class="site-footer">
    <p class="legal">© 2013 Company Name.&nbsp; All right reserved. Term of Use</p>
    <div class="social" aria-label="Social links"><span></span><span></span><span></span></div>
  </footer>
</body>
</html>
```